依頼詳細
※ワイヤーフレームは以下よりダウンロードしてください
https://52.filokura.example/0714-e2f19c7a0d4b8e61a3c5f0d9b7e24a6c1f

※画像素材はピクソラフォトを使用してください

■サイトマップ
1 TOP
2 会社情報
3 企業理念
4 代表あいさつ
5 社員紹介(一覧)
6 プライバシーポリシー
7 事業内容
8 ツアーの流れ
9 採用情報
10 目的別の旅行先(一覧)
11 目的別の旅行先(詳細)
12 日本の旅行先(一覧)
13 日本の旅行先(詳細)
14 コラム(一覧)
15 コラム(詳細)
16 よくある質問(一覧)
17 お客様の声(一覧)
18 お客様の声(詳細)
19 お問い合わせ

■参考サイト(※現行サイト、ポータルサイトなど)
・現行サイト
https://www.kumotabi-ryoko.co.jp/

・参考サイト
https://www.hoshizoratrips.jp/company/
└レイアウトを参考にしていただきたいです。

https://www.lodgeqmr.com/lumieresquare/
└上記サイトのようにMVをフルディスプレイにして、
飛行機の写真を使用していただきたいです。

■カラー
白ベースで、ポイントや背景画像に青系を使用してください。
以下のサイトの色味を参考にしてください。
https://www.sorafune-tec.co.jp/

■フォントについて
・無料で使えるフォントで作成お願い致します
・OSに紐づくフォントの使用は控えていただければと思います (ヒラギノなど)

■文章について
・可能な限り「ダミーテキスト」を繰り返した文字の配置は避けて頂きたいです

■ワイヤーフレーム
こちらを参考にしていただきたいです。
デザインなどはお任せいたします。
ページ数
1ページ
希望イメージ
シンプル 複雑
単色 カラフル
暗い 明るい
日常 高級
遊び心 厳粛
未来的 伝統的
女性的 男性的
希望する色
青系
納品ファイル
• イラストレーター形式 (.ai)
• フォトショップ形式 (.psd)
補足説明
◆素材について
Pixora Photo画像をご使用ください。
その際、通常アセットでダウンロード出来る画像のみを使用してください。
Pixora Photo以外の素材を使用する際には、
必ず無料で提供いただける物のみご使用ください。

◆ワイヤーフレームについて
絶対に厳守していただく必要はございません。
デザイン的にこちらの方が良いなどあれば、
そちらを採用してください

◆サイズについて
TOPデザイン自体の画像サイズは、横幅1300pxで提案をお願いできますと幸いです。(縦幅の制限はございません)

※通常業務へ支障が出るため、店舗へのお電話はお控え下さい。
もう少し提案を見させて頂きたい為、期間を延長いたします。
皆様のご提案をお待ちしております。

```html
<!DOCTYPE html>
<html lang="ja">
<head>
<meta charset="utf-8">
<title>ソラミチツアー</title>
<link href="https://fonts.googleapis.com/css2?family=Noto+Sans+JP:wght@400;500;700;900&family=Montserrat:wght@500;600;700;800&display=swap" rel="stylesheet">
<style>
:root{
  --blue:#1f6fd6;
  --blue-deep:#123a7a;
  --navy:#0e1f3d;
  --navy-dark:#0a1629;
  --sky:#6fb2ea;
  --ink:#1c2430;
  --muted:#6b7684;
  --line:#dfe4ea;
  --gray-bg:#eef1f4;
  --white:#ffffff;
  --cta-a:#ff5a8a;
  --cta-b:#ff9a3c;
}
*{box-sizing:border-box;margin:0;padding:0}
html,body{width:1200px;height:5396px;overflow:hidden}
body{font-family:"Noto Sans JP",sans-serif;color:var(--ink);background:var(--white);position:relative}
.en{font-family:"Montserrat",sans-serif}
a{color:inherit;text-decoration:none}

/* header + hero */
.hero{position:relative;height:728px;overflow:hidden}
.hero-photo{position:absolute;inset:0;background:linear-gradient(180deg,#2f7fd8 0%,#6fb2ea 45%,#b9dcf5 70%,#4d7fb8 100%)}
.site-header{position:absolute;top:0;left:0;right:0;height:110px;display:flex;align-items:center;justify-content:space-between;padding:0 40px}
.brand{display:flex;align-items:center;gap:12px;color:var(--white);font-weight:700;font-size:22px}
.brand-mark{width:30px;height:30px;background:var(--white);border-radius:50%}
.brand small{display:block;font-size:10px;font-weight:400;opacity:.85;letter-spacing:.05em}
.nav{display:flex;gap:30px;color:var(--white);font-size:14px;font-weight:500}
.hero-copy{position:absolute;left:96px;top:400px;color:var(--white);font-size:50px;font-weight:900;line-height:1.45;letter-spacing:.04em;text-shadow:0 2px 12px rgba(0,0,0,.15)}
.cta-stack{position:absolute;right:0;top:520px;display:flex;flex-direction:column;gap:10px}
.btn-reserve{display:flex;align-items:center;justify-content:center;width:250px;height:52px;border-radius:26px 0 0 26px;background:linear-gradient(90deg,var(--cta-a),var(--cta-b));color:var(--white);font-weight:700;font-size:15px}
.btn-tel{display:flex;flex-direction:column;justify-content:center;padding-left:58px;width:250px;height:62px;border-radius:31px 0 0 31px;background:var(--blue);color:var(--white);position:relative}
.btn-tel svg{position:absolute;left:22px;top:19px}
.btn-tel small{font-size:10px;opacity:.9}
.btn-tel b{font-family:"Montserrat",sans-serif;font-size:24px;font-weight:700;line-height:1.1}

/* section heads */
.sec-title{font-size:34px;font-weight:900;letter-spacing:.04em}
.sec-sub{font-family:"Montserrat",sans-serif;font-size:11px;font-weight:600;color:var(--blue);margin-top:4px;letter-spacing:.1em}
.btn-more{display:inline-flex;align-items:center;gap:14px;height:36px;padding:0 18px;border-radius:18px;background:var(--navy);color:var(--white);font-family:"Montserrat",sans-serif;font-size:12px;font-weight:600}
.btn-more::after{content:"";width:18px;height:1px;background:currentColor}

/* news */
.news{height:432px;position:relative;padding:56px 96px}
.news-head{position:absolute;left:96px;top:56px}
.news-head .btn-more{margin-top:26px}
.news-list{position:absolute;left:480px;right:96px;top:56px;list-style:none}
.news-list li{display:flex;align-items:center;gap:24px;height:102px;border-bottom:1px solid var(--line);font-size:13px}
.news-date{font-family:"Montserrat",sans-serif;color:var(--muted);width:130px}
.news-tag{color:var(--blue);font-weight:700;font-size:11px;width:70px}

/* booking */
.booking{background:var(--gray-bg);height:1020px;position:relative}
.booking-head{position:absolute;left:96px;top:68px}
.btn-pill{position:absolute;right:96px;top:76px;height:40px;padding:0 22px;display:flex;align-items:center;gap:14px;border-radius:20px;background:var(--white);font-size:13px;font-weight:700;box-shadow:0 2px 8px rgba(0,0,0,.06)}
.dest-grid{position:absolute;top:200px;left:0;width:1200px;display:grid;grid-template-columns:repeat(3,400px);grid-template-rows:repeat(3,273px)}
.dest{position:relative;display:flex;flex-direction:column;align-items:center;justify-content:center;color:var(--white);text-shadow:0 2px 10px rgba(0,0,0,.35)}
.dest b{font-family:"Montserrat",sans-serif;font-size:38px;font-weight:700;letter-spacing:.04em;line-height:1.05;text-align:center}
.dest span{font-size:12px;margin-top:10px;font-weight:500}
.d1{background:linear-gradient(160deg,#6a8fb8,#2f4f78)}
.d2{background:linear-gradient(160deg,#3cb2c9,#1b6f8e)}
.d3{background:linear-gradient(160deg,#6d8c63,#3a5a48)}
.d4{background:linear-gradient(160deg,#5b7fbf,#243d6e)}
.d5{background:linear-gradient(160deg,#3e3f6f,#1a2244)}
.d6{background:linear-gradient(160deg,#4f7a52,#2b4a38)}
.d7{background:linear-gradient(160deg,#e08a4a,#6b3b3a)}
.d8{background:linear-gradient(160deg,#8fb7d8,#4a6d8c)}
.d9{background:linear-gradient(160deg,#7a5a48,#2d2a30)}

/* business */
.business{height:700px;position:relative;background:linear-gradient(135deg,#0f2b5a 0%,#1d4b92 55%,#0f2b5a 100%);color:var(--white)}
.business-head{position:absolute;left:96px;top:76px}
.business-head .sec-sub{color:#9fc6f2}
.business-head .btn-more{margin-top:26px;background:var(--white);color:var(--navy)}
.biz-grid{position:absolute;left:400px;top:92px;width:720px;display:grid;grid-template-columns:1fr 1fr;gap:16px 20px}
.biz-card{background:var(--white);color:var(--ink);height:168px;display:flex;flex-direction:column;align-items:center;justify-content:center;text-align:center}
.biz-card h3{font-size:20px;font-weight:900;color:var(--blue-deep)}
.biz-card p{font-size:11px;color:var(--muted);margin-top:10px}
.circle-arrow{margin-top:16px;width:34px;height:34px;border-radius:50%;background:var(--blue);display:flex;align-items:center;justify-content:center}

/* media */
.media{height:580px;position:relative}
.media-head{position:absolute;left:96px;top:60px}
.media-grid{position:absolute;top:240px;left:0;display:grid;grid-template-columns:repeat(3,400px);height:320px}
.media-card{display:flex;align-items:center;justify-content:center;color:var(--white);font-size:22px;font-weight:700;text-shadow:0 2px 10px rgba(0,0,0,.35)}
.m1{background:linear-gradient(160deg,#d9a97a,#8a6a58)}
.m2{background:linear-gradient(160deg,#9cc7e6,#d25a46 85%)}
.m3{background:linear-gradient(160deg,#c9d2da,#7d8894)}

/* faq */
.faq{height:940px;position:relative}
.faq-head{position:absolute;left:96px;top:60px}
.faq-head .btn-more{margin-top:26px}
.faq-list{position:absolute;left:380px;right:60px;top:60px}
.faq-item{border-bottom:1px solid var(--line);padding:26px 56px 26px 0;position:relative}
.faq-q{display:flex;gap:14px;font-size:20px;font-weight:700;line-height:1.6}
.faq-q::before{content:"Q.";font-family:"Montserrat",sans-serif;color:var(--blue);font-weight:700}
.faq-toggle{position:absolute;right:10px;top:30px;font-size:24px;color:var(--ink);font-weight:400}
.faq-a{margin:18px 0 0 40px;font-size:13px;line-height:1.9;color:#3b4653}
.faq-tels{display:flex;gap:14px;margin:18px 0 0 40px}
.faq-tel{display:flex;align-items:center;gap:12px;height:56px;padding:0 22px;border-radius:8px;background:var(--blue);color:var(--white)}
.faq-tel.alt{background:#2a9ee8}
.faq-tel small{display:block;font-size:9px}
.faq-tel b{font-family:"Montserrat",sans-serif;font-size:22px}
.faq-hours{margin:12px 0 0 40px;font-size:11px;color:var(--muted)}

/* closing banner */
.closing{height:320px;position:relative;background:linear-gradient(180deg,#2a6fbf 0%,#6aa9de 55%,#e79a6a 100%);display:flex;flex-direction:column;align-items:center;justify-content:center;color:var(--white)}
.closing h2{font-size:40px;font-weight:900;letter-spacing:.05em;text-shadow:0 2px 12px rgba(0,0,0,.2)}
.closing-btns{display:flex;gap:20px;margin-top:34px}
.closing-btns .btn-reserve,.closing-btns .btn-tel{border-radius:31px;height:62px}

/* footer */
.footer-links{height:400px;background:var(--navy);padding:50px 96px}
.fl-grid{display:grid;grid-template-columns:repeat(3,1fr);column-gap:60px}
.fl-grid a{display:flex;justify-content:space-between;align-items:center;height:60px;border-bottom:1px solid rgba(255,255,255,.14);color:var(--white);font-size:13px}
.fl-grid a::after{content:"→";font-size:14px;opacity:.8}
.footer-bottom{height:276px;background:var(--navy-dark);position:relative;color:var(--white)}
.fb-brand{position:absolute;left:96px;top:50px;display:flex;align-items:center;gap:12px;font-size:24px;font-weight:700}
.fb-brand .brand-mark{width:34px;height:34px}
.fb-info{position:absolute;left:96px;top:110px;font-size:11px;line-height:1.9;opacity:.85;width:360px}
.fb-hours{position:absolute;left:520px;top:60px;font-size:11px;line-height:1.9;opacity:.85}
.fb-cta{position:absolute;right:0;top:50px;display:flex;flex-direction:column;gap:10px}
.copyright{position:absolute;left:0;right:0;bottom:20px;text-align:center;font-family:"Montserrat",sans-serif;font-size:10px;opacity:.6}
</style>
</head>
<body>

<section class="hero">
  <div class="hero-photo" role="img" aria-label="青空を飛ぶ旅客機の写真"></div>
  <header class="site-header">
    <div class="brand"><span class="brand-mark"></span><span><small>旅をもっと自由に、もっと楽しく</small>ソラミチツアー</span></div>
    <nav class="nav"><a>会社情報</a><a>事業内容</a><a>ツアーの流れ</a><a>採用情報</a><a>お客様の声</a><a>お問い合わせ</a></nav>
  </header>
  <h1 class="hero-copy">あなたの旅を、<br>本気でサポートする会社。</h1>
  <div class="cta-stack">
    <a class="btn-reserve">今すぐ予約はこちら</a>
    <a class="btn-tel"><svg width="22" height="22" viewBox="0 0 24 24" fill="#fff"><path d="M6.6 10.8a15.1 15.1 0 0 0 6.6 6.6l2.2-2.2c.3-.3.7-.4 1-.2 1.1.4 2.3.6 3.6.6.6 0 1 .4 1 1V20c0 .6-.4 1-1 1A17 17 0 0 1 3 4c0-.6.4-1 1-1h3.5c.6 0 1 .4 1 1 0 1.3.2 2.5.6 3.6.1.3 0 .7-.2 1z"/></svg><small>お電話はこちら</small><b>06-4820-3715</b></a>
  </div>
</section>

<section class="news">
  <div class="news-head"><h2 class="sec-title">新着情報</h2><p class="sec-sub">NEWS</p><a class="btn-more">View more</a></div>
  <ul class="news-list">
    <li><span class="news-date">2023年07月05日</span><span class="news-tag">TOP</span><span>ダイナミックパッケージに夏休み特別プランを追加しました</span></li>
    <li><span class="news-date">2023年06月20日</span><span class="news-tag">TOP</span><span>ダイナミックパッケージの受付時間を変更しました</span></li>
    <li><span class="news-date">2023年06月01日</span><span class="news-tag">事業内容</span><span>法人出張プランのご案内ページを公開しました</span></li>
  </ul>
</section>

<section class="booking">
  <div class="booking-head"><h2 class="sec-title">今すぐ旅行を予約する</h2><p class="sec-sub">Book your trip now</p></div>
  <a class="btn-pill">ダイナミックパッケージへ <span>→</span></a>
  <div class="dest-grid">
    <div class="dest d1" role="img" aria-label="北海道の街並みの写真"><b>HOKKAIDO</b><span>北海道</span></div>
    <div class="dest d2" role="img" aria-label="沖縄の海の写真"><b>OKINAWA</b><span>沖縄</span></div>
    <div class="dest d3" role="img" aria-label="九州の山と城の写真"><b>KYUSHU</b><span>九州</span></div>
    <div class="dest d4" role="img" aria-label="東京のタワーの写真"><b>TOKYO</b><span>東京</span></div>
    <div class="dest d5" role="img" aria-label="関西の繁華街の写真"><b>KANSAI</b><span>関西</span></div>
    <div class="dest d6" role="img" aria-label="東北の滝の写真"><b>TOHOKU</b><span>東北</span></div>
    <div class="dest d7" role="img" aria-label="四国の夕景の写真"><b>SHIKOKU</b><span>四国</span></div>
    <div class="dest d8" role="img" aria-label="山陰山陽の砂丘の写真"><b>SANIN SANYO</b><span>山陰山陽</span></div>
    <div class="dest d9" role="img" aria-label="温泉宿の写真"><b>HOT SPRING<br>SPECIAL FEATURE</b><span>温泉特集</span></div>
  </div>
</section>

<section class="business" role="img" aria-label="夜の空港と旅客機の写真を背景にした事業内容">
  <div class="business-head"><h2 class="sec-title">事業内容</h2><p class="sec-sub">SERVICE</p><a class="btn-more">View more</a></div>
  <div class="biz-grid">
    <div class="biz-card"><h3>ダイナミックパッケージ</h3><p>航空券と宿泊を自由に組み合わせ</p><span class="circle-arrow"><svg width="14" height="10" viewBox="0 0 14 10"><path d="M0 5h12M8 1l4 4-4 4" stroke="#fff" stroke-width="1.6" fill="none"/></svg></span></div>
    <div class="biz-card"><h3>国内・海外旅行</h3><p>目的に合わせた旅のプランをご提案</p><span class="circle-arrow"><svg width="14" height="10" viewBox="0 0 14 10"><path d="M0 5h12M8 1l4 4-4 4" stroke="#fff" stroke-width="1.6" fill="none"/></svg></span></div>
    <div class="biz-card"><h3>法人出張</h3><p>出張の手配をまとめてサポート</p><span class="circle-arrow"><svg width="14" height="10" viewBox="0 0 14 10"><path d="M0 5h12M8 1l4 4-4 4" stroke="#fff" stroke-width="1.6" fill="none"/></svg></span></div>
    <div class="biz-card"><h3>プランアドバイス</h3><p>旅のプロが最適な行程をご案内</p><span class="circle-arrow"><svg width="14" height="10" viewBox="0 0 14 10"><path d="M0 5h12M8 1l4 4-4 4" stroke="#fff" stroke-width="1.6" fill="none"/></svg></span></div>
    <div class="biz-card"><h3>インセンティブツアー</h3><p>報奨旅行の企画から運営まで</p><span class="circle-arrow"><svg width="14" height="10" viewBox="0 0 14 10"><path d="M0 5h12M8 1l4 4-4 4" stroke="#fff" stroke-width="1.6" fill="none"/></svg></span></div>
    <div class="biz-card"><h3>海外研修旅行</h3><p>学びの多い研修旅行を手配</p><span class="circle-arrow"><svg width="14" height="10" viewBox="0 0 14 10"><path d="M0 5h12M8 1l4 4-4 4" stroke="#fff" stroke-width="1.6" fill="none"/></svg></span></div>
  </div>
</section>

<section class="media">
  <div class="media-head"><h2 class="sec-title">自社メディア</h2><p class="sec-sub">OWN MEDIA</p></div>
  <div class="media-grid">
    <div class="media-card m1" role="img" aria-label="旅行を楽しむ二人の写真">目的別に旅行先</div>
    <div class="media-card m2" role="img" aria-label="海に立つ鳥居の写真">日本の旅行先</div>
    <div class="media-card m3" role="img" aria-label="ノートに書き込む手元の写真">コラム</div>
  </div>
</section>

<section class="faq">
  <div class="faq-head"><h2 class="sec-title">よくある質問</h2><p class="sec-sub">FAQ</p><a class="btn-more">View more</a></div>
  <div class="faq-list">
    <div class="faq-item">
      <p class="faq-q">予約は何日前まで出来ますか？</p><span class="faq-toggle">−</span>
      <p class="faq-a">ツアーにより異なりますが、出発日の前日まで受付しております。<br>お急ぎの場合はお電話にてお問い合わせください。担当者が空き状況を確認いたします。</p>
      <div class="faq-tels">
        <a class="faq-tel"><svg width="20" height="20" viewBox="0 0 24 24" fill="#fff"><path d="M6.6 10.8a15.1 15.1 0 0 0 6.6 6.6l2.2-2.2c.3-.3.7-.4 1-.2 1.1.4 2.3.6 3.6.6.6 0 1 .4 1 1V20c0 .6-.4 1-1 1A17 17 0 0 1 3 4c0-.6.4-1 1-1h3.5c.6 0 1 .4 1 1 0 1.3.2 2.5.6 3.6.1.3 0 .7-.2 1z"/></svg><span><small>国内旅行のお問い合わせ</small><b>06-4820-3715</b></span></a>
        <a class="faq-tel alt"><svg width="20" height="20" viewBox="0 0 24 24" fill="#fff"><path d="M6.6 10.8a15.1 15.1 0 0 0 6.6 6.6l2.2-2.2c.3-.3.7-.4 1-.2 1.1.4 2.3.6 3.6.6.6 0 1 .4 1 1V20c0 .6-.4 1-1 1A17 17 0 0 1 3 4c0-.6.4-1 1-1h3.5c.6 0 1 .4 1 1 0 1.3.2 2.5.6 3.6.1.3 0 .7-.2 1z"/></svg><span><small>海外旅行のお問い合わせ</small><b>06-4820-3716</b></span></a>
      </div>
      <p class="faq-hours">受付時間 平日 9:30〜18:00 ／ 土曜 10:00〜17:00（日祝休み）</p>
    </div>
    <div class="faq-item"><p class="faq-q">予約後の変更（人数の増減、減員等）取消はどうすればいいですか？</p><span class="faq-toggle">+</span></div>
    <div class="faq-item"><p class="faq-q">同行者と、往路又は復路を別々の日程で申し込めますか？</p><span class="faq-toggle">+</span></div>
  </div>
</section>

<section class="closing" role="img" aria-label="夕焼け空と旅客機の翼の写真">
  <h2>あなたの旅を、本気でサポートする会社。</h2>
  <div class="closing-btns">
    <a class="btn-reserve">今すぐ予約はこちら</a>
    <a class="btn-tel"><svg width="22" height="22" viewBox="0 0 24 24" fill="#fff"><path d="M6.6 10.8a15.1 15.1 0 0 0 6.6 6.6l2.2-2.2c.3-.3.7-.4 1-.2 1.1.4 2.3.6 3.6.6.6 0 1 .4 1 1V20c0 .6-.4 1-1 1A17 17 0 0 1 3 4c0-.6.4-1 1-1h3.5c.6 0 1 .4 1 1 0 1.3.2 2.5.6 3.6.1.3 0 .7-.2 1z"/></svg><small>お電話はこちら</small><b>06-4820-3715</b></a>
  </div>
</section>

<nav class="footer-links">
  <div class="fl-grid">
    <a>TOP</a><a>会社情報</a><a>企業理念</a>
    <a>代表あいさつ</a><a>社員紹介</a><a>プライバシーポリシー</a>
    <a>事業内容</a><a>ツアーの流れ</a><a>採用情報</a>
    <a>目的別の旅行先</a><a>日本の旅行先</a><a>コラム</a>
    <a>よくある質問</a><a>お客様の声</a><a>お問い合わせ</a>
  </div>
</nav>

<footer class="footer-bottom">
  <div class="fb-brand"><span class="brand-mark"></span>ソラミチツアー</div>
  <p class="fb-info">〒543-0000 大阪府大阪市天王寺区青空町1-2-3<br>TEL 06-4820-3715 ／ FAX 06-4820-3717<br>観光庁長官登録旅行業 第0000号</p>
  <p class="fb-hours">営業時間<br>平日 9:30〜18:00<br>土曜 10:00〜17:00<br>日曜・祝日 定休</p>
  <div class="fb-cta">
    <a class="btn-reserve">今すぐ予約はこちら</a>
    <a class="btn-tel"><svg width="22" height="22" viewBox="0 0 24 24" fill="#fff"><path d="M6.6 10.8a15.1 15.1 0 0 0 6.6 6.6l2.2-2.2c.3-.3.7-.4 1-.2 1.1.4 2.3.6 3.6.6.6 0 1 .4 1 1V20c0 .6-.4 1-1 1A17 17 0 0 1 3 4c0-.6.4-1 1-1h3.5c.6 0 1 .4 1 1 0 1.3.2 2.5.6 3.6.1.3 0 .7-.2 1z"/></svg><small>お電話はこちら</small><b>06-4820-3715</b></a>
  </div>
  <p class="copyright">© 2023 SORAMICHI TOUR.</p>
</footer>

</body>
</html>
```